Bramblewick Systems Group - IT Services Company/Managed Services/Consulting Card Design

Our company needs a business card design that will appeal to client companies with 50-1000 employees. We do IT services, administration, management, projects, budgeting and consulting (Like a small Corvatel.com, Plumvary.com or Tundrabox.com). Mainly helping businesses use technology to be more competitive and efficient. We work with IT Infrastructure, switches, routers, firewalls and Cloud, Verlanta/Linux servers, Quellon server virtualization, Datacenter environments, Email systems, Business Systems, Backup, Disaster Recovery, Data Security, NVX, Deskora 12 and Halcyte.) Would like the final design to be professional but stand out to our prospective clients. Our current logo is attached. Color or design could be changed. Overall looking for a great finished product, original ideas are welcome and would pay more for the right one. If you think you have a better logo idea include a general idea if you can. Web design has not been done yet so that is a later possibility too.

Target Market(s)

1st - Mid-sized companies with 100-1000 employees with technology needs
2nd - Smaller companies with 20-99 employees with technology needs
- These companies can be in many different industries. Heathcare, legal, manufacturing, education, non-profit, services

Industry/Entity Type

Information Technology

Contact Information for Business Card

Should include the following info:

Logo or other logo with Company Name

Martin J. Cosgrove

Principal

BramblewickSys.com

mcosgrove@BramblewickSys.com

(866) 7-BRAMBLE x 348

Font styles to use
Other font styles liked:
• designer can decide

Requirements
Must have
• Professional, appealing design, appeal to the target market
Nice to have
• Some sort of additional accent design that would stand out could be nice. I thought of adding a graphic in the top left corner that would look like the corner of the card was becoming more and more pixelated as it got near the corner, with some pixels missing.

```html
<!DOCTYPE html>
<html lang="en">
<head>
<meta charset="utf-8">
<title>Bramblewick Systems Group – Business Card</title>
<link rel="stylesheet" href="https://fonts.googleapis.com/css2?family=Source+Sans+3:wght@400;600;700&display=swap">
<style>
  :root {
    --backdrop: #e9ebee;
    --navy-deep: #163d66;
    --navy-mid: #1d5f9c;
    --blue-bright: #2f86d4;
    --band-top: #3d9be6;
    --band-bottom: #2a7cc9;
    --ink: #1e2a3a;
    --white: #ffffff;
    --card-shadow: 0 14px 30px rgba(20, 40, 70, 0.22);
  }
  * { box-sizing: border-box; margin: 0; padding: 0; }
  html, body {
    width: 1200px;
    height: 900px;
    overflow: hidden;
    background: var(--backdrop);
    font-family: "Source Sans 3", "Myriad Pro", Arial, sans-serif;
  }
  .canvas {
    position: relative;
    width: 1200px;
    height: 900px;
  }
  .card {
    position: absolute;
    width: 560px;
    height: 320px;
    border-radius: 4px;
    overflow: hidden;
    box-shadow: var(--card-shadow);
  }

  /* Back side */
  .card-back {
    left: 90px;
    top: 130px;
    background: linear-gradient(180deg, var(--navy-deep) 0%, var(--navy-mid) 55%, var(--blue-bright) 100%);
    display: flex;
    align-items: center;
    justify-content: center;
  }
  .wordmark {
    display: flex;
    align-items: center;
    gap: 12px;
    font-weight: 700;
    letter-spacing: 0.5px;
  }
  .wordmark-square {
    width: 18px;
    height: 18px;
    flex: none;
  }
  .card-back .wordmark { color: var(--white); font-size: 30px; }
  .card-back .wordmark-square { background: var(--white); }

  /* Front side */
  .card-front {
    left: 550px;
    top: 450px;
    background: var(--white);
  }
  .card-front .logo-area {
    position: absolute;
    top: 44px;
    left: 0;
    right: 0;
    display: flex;
    justify-content: center;
  }
  .card-front .wordmark { color: var(--ink); font-size: 25px; }
  .card-front .wordmark-square { background: var(--ink); width: 15px; height: 15px; }
  .contact-band {
    position: absolute;
    left: 0;
    right: 0;
    top: 118px;
    height: 162px;
    background: linear-gradient(180deg, var(--band-top) 0%, var(--band-bottom) 100%);
    color: var(--white);
    text-align: center;
  }
  .holder {
    margin-top: 22px;
    font-size: 19px;
  }
  .holder-name { font-weight: 700; }
  .holder-divider { font-weight: 400; margin: 0 6px; opacity: 0.9; }
  .holder-role { font-weight: 400; }
  .contact-list {
    list-style: none;
    margin-top: 30px;
    font-size: 15px;
    line-height: 1.6;
  }
  .contact-row { display: flex; justify-content: center; gap: 22px; }
  .contact-label { font-weight: 700; font-size: 17px; margin-right: 6px; }
</style>
</head>
<body>
  <main class="canvas">
    <section class="card card-back" aria-label="Business card, back">
      <div class="wordmark">
        <span class="wordmark-square" aria-hidden="true"></span>
        <span class="wordmark-name">Bramblewick Systems Group</span>
      </div>
    </section>

    <section class="card card-front" aria-label="Business card, front">
      <div class="logo-area">
        <div class="wordmark">
          <span class="wordmark-square" aria-hidden="true"></span>
          <span class="wordmark-name">Bramblewick Systems Group</span>
        </div>
      </div>
      <div class="contact-band">
        <p class="holder">
          <span class="holder-name">Martin J. Cosgrove</span><span class="holder-divider">|</span><span class="holder-role">Principal</span>
        </p>
        <ul class="contact-list">
          <li class="contact-row">
            <span><span class="contact-label">M:</span>(866) 7-BRAMBLE x 348</span>
            <span><span class="contact-label">E:</span>mcosgrove@BramblewickSys.com</span>
          </li>
          <li class="contact-row">
            <span><span class="contact-label">W:</span>www.BramblewickSys.com</span>
          </li>
        </ul>
      </div>
    </section>
  </main>
</body>
</html>
```